International Medical Company Needs a Website Design for a Support Site

We need a website design for a support site we are doing for ostomates called Bright Rebounds. We are an international company but this website is for our Australian market.

The website is a support site for people who are living with an Ostomy or Bowel Disease. This is a site where they can read other ostomates' stories and how they are dealing with the fact that they have to wear a pouch everyday.

The URL for our US site is: http://www.brightrebounds-example.com/

We need to use the same logo but we have freedom around the color scheme. We are not fond of the brown color scheme used in our US site and are happy for designs to be submitted with alternatives.

• We want the design to be clean, inspiring, modern and inviting.
• We would like to see a design for the mainpage / homepage and one of the subpages
• We only require the PSD / image files (no HTML needed)

Attached to this project is our sitemap, an example wireframe and the logos. We are happy for you to play around with different options and don't have to stick to the layout shown in the wireframe.

If you have any further questions please ask.

```html
<!DOCTYPE html>
<html lang="en">
<head>
<meta charset="utf-8">
<title>Bright Rebounds</title>
<link rel="stylesheet" href="https://fonts.googleapis.com/css2?family=Open+Sans:ital,wght@0,400;0,600;1,400;1,600&family=Arimo:wght@400&family=Tinos:ital,wght@0,400;1,700&family=Roboto+Condensed:wght@400&display=swap">
<style>
:root{
  --brown:#8a5a1c;
  --gold:#9b7a45;
  --ink:#3d3d3d;
  --muted:#6f6f6f;
  --panel:#3b3b3b;
  --nav:#3a3a3a;
  --footer:#4a4a4a;
  --rule:#e3e3e3;
  --white:#ffffff;
}
*{margin:0;padding:0;box-sizing:border-box}
html,body{width:1200px;height:1067px;overflow:hidden;background:var(--white)}
body{position:relative;font-family:"Open Sans",sans-serif;color:var(--ink)}
.abs{position:absolute}

.brand{left:131px;top:126px;display:flex;align-items:center;gap:8px}
.brand-dot{width:12px;height:12px;border-radius:50%;background:var(--gold)}
.brand-name{font-family:"Open Sans",sans-serif;font-weight:600;font-size:15.5px;letter-spacing:1.6px;color:var(--brown)}

.country-label{left:708px;top:52px;font-size:12.5px;color:var(--brown)}
.country-select{left:840px;top:43px;width:228px;height:36px;border:1px solid #dcdcdc;background:#f7f7f7;font-size:11.5px;color:#777;padding:10px 12px}
.country-select svg{position:absolute;right:10px;top:14px}

.main-nav{left:330px;top:98px;width:739px;height:50px;border-radius:5px;background:linear-gradient(#4a4a4a,#2e2e2e);box-shadow:0 2px 3px rgba(0,0,0,.3);display:flex;align-items:center;justify-content:space-around;padding:0 10px}
.main-nav a{color:#f2f2f2;text-decoration:none;font-size:13.6px}

.intro-panel{left:131px;top:160px;width:323px;height:389px;background:var(--panel)}
.intro-title{left:17px;top:50px;font-family:"Tinos",serif;font-size:15.5px;color:var(--white);letter-spacing:.3px}
.intro-rule{left:13px;top:76px;width:297px;height:4px;border-top:1px solid #ddd;border-bottom:1px solid #ddd}
.intro-text{left:18px;top:104px;width:300px;font-style:italic;font-weight:600;font-size:10.2px;line-height:27.2px;color:var(--white)}
.btn{top:291px;height:38px;border-radius:5px;background:linear-gradient(#fafafa,#d6d6d6);font-family:"Tinos",serif;font-style:italic;font-weight:700;font-size:12px;color:#444;display:flex;align-items:center;justify-content:center;letter-spacing:.3px}
.btn-share{left:16px;width:119px}
.btn-read{left:187px;width:120px}
.btn-or{left:150px;top:300px;font-family:"Tinos",serif;font-style:italic;font-weight:700;font-size:12.5px;color:var(--white)}

.hero{left:457px;top:160px;width:612px;height:389px;background:linear-gradient(180deg,#7f9bb5 0%,#b9cde0 45%,#6d7f90 75%,#2a2a2a 100%)}
.hero-arrow{top:350px;width:22px;height:22px;background:#e8e8e8;border:1px solid #999;display:flex;align-items:center;justify-content:center}

.section-title{top:567px;font-style:italic;font-weight:600;font-size:19px;color:#444}
.photo{background:linear-gradient(135deg,#3d5c5c,#6b7d6e 50%,#2f3f45)}

.feature-title{left:131px;top:773px;font-size:14px;color:var(--brown)}
.feature-text{left:132px;top:800px;width:300px;font-size:11.5px;line-height:25.6px;color:var(--muted)}
.feature-text a{color:var(--brown);text-decoration:none}

.story-link{left:478px;font-size:12px;color:var(--brown)}
.story-text{left:479px;width:280px;font-size:11.3px;line-height:21.6px;color:var(--muted)}
.avatar{left:482px;top:836px;width:96px;height:96px;border-radius:50%;border:2px solid #ddd;background:linear-gradient(#8a6a4a,#c9a98a)}
.avatar-name{left:602px;top:862px;font-family:"Roboto Condensed",sans-serif;font-size:17px;color:var(--brown)}
.avatar-date{left:602px;top:890px;font-family:"Arimo",sans-serif;font-size:11.5px;color:#555}

.news-item{left:788px;width:281px;height:118px;border-bottom:2px solid var(--rule)}
.news-thumb{left:0;top:0;width:77px;height:79px}
.news-date{left:90px;top:2px;font-size:12px;color:var(--brown)}
.news-text{left:90px;top:24px;width:190px;font-family:"Arimo",sans-serif;font-size:10.2px;line-height:19.6px;color:#666}
.news-text a{color:var(--brown);text-decoration:none}

.site-footer{left:0;top:973px;width:1200px;height:94px;background:var(--footer)}
.copyright{left:133px;top:37px;font-size:11.5px;color:var(--white)}
.social{top:32px;width:32px;height:32px;border-radius:50%;border:2px solid var(--white)}
</style>
</head>
<body>

<div class="brand abs">
  <span class="brand-dot"></span>
  <span class="brand-name">BRIGHT REBOUNDS</span>
</div>

<div class="country-label abs">Choose Your Country:</div>
<div class="country-select abs">United States
  <svg width="11" height="8" viewBox="0 0 11 8"><path d="M0 0h11L5.5 8z" fill="#555"/></svg>
</div>

<nav class="main-nav abs">
  <a>About Us</a><a>Personal Stories</a><a>Tips For Living</a><a>News</a><a>Resources</a><a>Contact Us</a><a>Search</a>
</nav>

<section class="intro-panel abs">
  <h1 class="intro-title abs" style="font-weight:400">SHARING STORIES AND GIVING HOPE</h1>
  <div class="intro-rule abs"></div>
  <p class="intro-text abs">Congratulations to Martin Okafor of Fairhaven, MD, named this year’s Bright Rebounds® National Award recipient at at the Continence Care Nurses Society National Award recipient&nbsp; Nurses It is hard to believe that Bright Rebounds old now but it is! Looking back it was the diagnosis of my Inflammatory Bowe.......</p>
  <div class="btn btn-share abs">SHARE A STORY</div>
  <div class="btn-or abs">(OR)</div>
  <div class="btn btn-read abs">READ STORIES</div>
</section>

<div class="hero abs" role="img" aria-label="Hand-lettered quote about happiness in giving, over a photo of a climber helping another up a rock at sunrise">
  <div class="hero-arrow abs" style="left:551px"><svg width="10" height="12"><path d="M7 1L2 6l5 5" stroke="#444" stroke-width="2" fill="none"/></svg></div>
  <div class="hero-arrow abs" style="left:580px"><svg width="10" height="12"><path d="M3 1l5 5-5 5" stroke="#444" stroke-width="2" fill="none"/></svg></div>
</div>

<h2 class="section-title abs" style="left:131px">What is Bright Re bounds</h2>
<h2 class="section-title abs" style="left:478px">Share a Story</h2>
<h2 class="section-title abs" style="left:802px">Latest News</h2>

<div class="photo abs" style="left:131px;top:614px;width:284px;height:144px" role="img" aria-label="Smiling couple posing in front of a painted backdrop"></div>
<h3 class="feature-title abs" style="font-weight:400">Life-long educator and avid outdoorsman</h3>
<p class="feature-text abs">There are many variations of passages of Lorem Ipsum available, but the majority have suffered alteration in some form, by injected humour, or randomised&nbsp; even slightly believable. <a>[Read More ]</a></p>

<h3 class="story-link abs" style="top:614px;font-weight:400">A Message from Daniel Ashworth</h3>
<p class="story-text abs" style="top:643px">LARCHMONT, NJ October 19, 2012 - The Bright Rebounds® Program has named Martin (Marty) Okafor of Fairhaven, Maryland .........</p>
<h3 class="story-link abs" style="top:730px;left:477px;font-weight:400">Make Your Voice World Ostomy Day</h3>
<p class="story-text abs" style="top:758px">LARCHMONT, NJ October 19, 2012 - The Bright Rebounds® Program has named Martin (Marty) Okafor of Fairhaven, Maryland .........</p>
<div class="avatar abs" role="img" aria-label="Portrait of story author"></div>
<div class="avatar-name abs">Clara Whitfield</div>
<div class="avatar-date abs">on 22 Feb 2014</div>

<article class="news-item abs" style="top:620px">
  <div class="news-thumb photo abs" style="background:linear-gradient(#b8b8b8,#8aa0b8)" role="img" aria-label="Portrait of award recipient"></div>
  <div class="news-date abs">[ August 21, 2013 ]</div>
  <p class="news-text abs">Congratulations to Martin Okafor of Fairhaven, MD, named this year's Bright.... <a>Read More</a></p>
</article>
<article class="news-item abs" style="top:737px">
  <div class="news-thumb photo abs" style="background:linear-gradient(#7aa0c8,#b02020 60%,#222)" role="img" aria-label="Outdoor expedition photo"></div>
  <div class="news-date abs">[ August 21, 2013 ]</div>
  <p class="news-text abs">Congratulations to Martin Okafor of Fairhaven, MD, named this year's Bright.... <a>Read More</a></p>
</article>
<article class="news-item abs" style="top:852px">
  <div class="news-thumb photo abs" style="background:linear-gradient(90deg,#d9b890,#6a4a30 60%,#e07020)" role="img" aria-label="Two event participants outdoors"></div>
  <div class="news-date abs">[ August 21, 2013 ]</div>
  <p class="news-text abs">Congratulations to Martin Okafor of Fairhaven, MD, named this year's Bright.... <a>Read More</a></p>
</article>

<footer class="site-footer abs">
  <div class="copyright abs">Copyright 2014 Bright Rebounds.All Right Reseved.</div>
  <div class="social abs" style="left:886px"></div>
  <div class="social abs" style="left:922px"></div>
  <div class="social abs" style="left:958px"></div>
  <div class="social abs" style="left:994px"></div>
  <div class="social abs" style="left:1027px"></div>
</footer>

</body>
</html>
```